Attract renters to our neighborhoods - inform renters who we are

Apartments in several neighborhoods. We want to attract renters who want to live along the lake or other near by neighborhoods. We want them to know that we have an apartment for them in their location.
The perfect location to spend your time.
When minutes matter LIVE where you work and play! (love this tag line)
Updates

www.kvtresidences.example Choose from over 3,700 apartments in Chicago’s most celebrated neighborhoods. 773-582-6041 Chicago’s most celebrated neighborhoods. 31 PROPERTIES

Target Market(s)

Sophisticated apartment renter who wants location, space, amenities

Industry/Entity Type

Apartment Rentals

Requirements
Must have
• Feel like I want to live there, or the ad is calling me
Nice to have
• Appeal to a sophisticated apartment renter. We have what you want, where you want to be.
Should not have
• Logo colors are black and red/burnt orange see attached logo

```html
<!DOCTYPE html>
<html lang="en">
<head>
<meta charset="utf-8">
<title>KVT Residences – The Perfect Location</title>
<link href="https://fonts.googleapis.com/css2?family=Archivo+Black&family=Montserrat:wght@600;700;800;900&family=Oswald:wght@500;600&family=Roboto+Condensed:wght@700&display=swap" rel="stylesheet">
<style>
  :root {
    --stage: #2b2b2b;
    --paper: #ffffff;
    --red: #c8102e;
    --deep-red: #7d0d12;
    --ink: #1b1b1b;
    --panel: #2c2b31;
    --map: #34363b;
  }
  * { margin: 0; padding: 0; box-sizing: border-box; }
  html, body { width: 1200px; height: 1177px; overflow: hidden; background: var(--stage); }
  .flyer {
    position: absolute; left: 245px; top: 103px;
    width: 751px; height: 973px; background: var(--paper); overflow: hidden;
    font-family: "Montserrat", sans-serif;
  }
  .abs { position: absolute; }
  .headline {
    left: 22px; top: 14px; font-family: "Archivo Black", sans-serif;
    font-size: 55px; line-height: 58px; letter-spacing: 0.5px;
  }
  .headline .l1 { color: var(--red); display: block; }
  .headline .l2 { color: var(--deep-red); display: block; }
  .tag-box {
    left: 22px; top: 140px; width: 324px; height: 54px; background: var(--ink);
    color: #fff; font-family: "Oswald", sans-serif; font-weight: 500;
    font-size: 33px; line-height: 54px; text-align: center;
  }
  .lede {
    left: 22px; top: 212px; color: var(--ink); font-weight: 600;
    font-size: 20px; line-height: 29px;
  }
  .work-play {
    left: 20px; top: 272px; font-family: "Archivo Black", sans-serif;
    font-size: 53px; line-height: 54px;
  }
  .work-play .w { color: var(--deep-red); display: block; }
  .work-play .p { color: var(--red); display: block; }
  .hero-art { left: 0; top: 0; }
  .thumbs { left: 13px; top: 398px; width: 726px; height: 113px; display: flex; gap: 14px; }
  .thumb { flex: 1; }
  .thumb.skyline { background: linear-gradient(180deg, #8fbde6 0%, #c7d6e2 30%, #5d6770 50%, #8a8f92 65%, #2aa8b8 100%); }
  .thumb.towers { background: linear-gradient(170deg, #7db4e4 0%, #b9cfe0 22%, #7b8794 45%, #a9a59c 75%, #6e6a63 100%); }
  .thumb.beach { background: linear-gradient(180deg, #9cc7ea 0%, #d5e3ea 20%, #3f7a6a 34%, #26b3c1 55%, #e3d3b0 72%, #1fa5b7 100%); }
  .thumb.harbor { background: linear-gradient(180deg, #98c3e8 0%, #d3dde4 22%, #8a8c85 42%, #4f7d52 62%, #27aab8 100%); }
  .dark-band { left: 0; top: 521px; width: 751px; height: 254px; background: var(--panel); }
  .map { left: 0; top: 521px; width: 433px; height: 254px; background: radial-gradient(ellipse at 60% 45%, #44464c 0%, #35373c 55%, #2d2f34 100%); }
  .choose { right: 14px; top: 572px; text-align: right; color: #fff; }
  .choose .big { font-family: "Archivo Black", sans-serif; color: var(--red); font-size: 56px; line-height: 56px; display: block; }
  .choose .sub { font-weight: 600; font-size: 29px; line-height: 31px; display: block; }
  .choose .hood { font-weight: 900; font-size: 41px; line-height: 52px; display: block; letter-spacing: 0.5px; }
  .phone-icon { left: 366px; top: 795px; }
  .phone-number {
    left: 262px; top: 860px; width: 260px; text-align: center;
    font-family: "Roboto Condensed", sans-serif; font-weight: 700;
    font-size: 36px; line-height: 40px; color: var(--ink);
  }
  .brand {
    left: 528px; top: 810px; display: flex; align-items: center; gap: 10px;
    font-family: "Archivo Black", sans-serif; font-size: 76px; line-height: 84px; color: var(--ink);
  }
  .brand .mark { width: 22px; height: 22px; background: var(--red); }
  .url-bar {
    left: 0; top: 914px; width: 751px; height: 59px; background: var(--red);
    color: #fff; font-weight: 700; font-size: 26px; line-height: 59px;
    text-align: center; padding-left: 34px; letter-spacing: 0.3px;
  }
</style>
</head>
<body>
<main class="flyer">
  <svg class="abs hero-art" width="751" height="390" viewBox="0 0 751 390">
    <defs>
      <linearGradient id="room" x1="0" y1="0" x2="0" y2="1">
        <stop offset="0" stop-color="#f3f3f2"/>
        <stop offset="0.35" stop-color="#e6e8ea"/>
        <stop offset="0.6" stop-color="#cfd3d8"/>
        <stop offset="0.78" stop-color="#b9b4ad"/>
        <stop offset="1" stop-color="#9c6a42"/>
      </linearGradient>
    </defs>
    <polygon role="img" aria-label="Bright living room with grey sofa, wood floor and city-view windows"
      points="523,0 751,0 751,385 259,385" fill="url(#room)"/>
    <polygon points="488,0 514,0 346,265 320,265" fill="var(--red)"/>
  </svg>

  <h1 class="abs headline"><span class="l1">THE PERFECT</span><span class="l2">LOCATION</span></h1>
  <div class="abs tag-box">TO SPEND YOUR TIME!</div>
  <p class="abs lede">When minutes matter...<br>LIVE where you</p>
  <p class="abs work-play"><span class="w">WORK &amp;</span><span class="p">PLAY!</span></p>

  <div class="abs thumbs">
    <div class="thumb skyline" role="img" aria-label="Aerial view of downtown skyline and lakefront"></div>
    <div class="thumb towers" role="img" aria-label="Aerial view of high-rises along the lake"></div>
    <div class="thumb beach" role="img" aria-label="Aerial view of a curved lakeside beach"></div>
    <div class="thumb harbor" role="img" aria-label="Aerial view of harbor and lakeshore park"></div>
  </div>

  <div class="abs dark-band"></div>
  <div class="abs map" role="img" aria-label="Dark street map of city neighborhoods with red property pins"></div>

  <svg class="abs" style="left:0;top:521px" width="440" height="392" viewBox="0 0 440 392">
    <defs>
      <linearGradient id="hand" x1="0" y1="0" x2="1" y2="1">
        <stop offset="0" stop-color="#c3ccd5"/>
        <stop offset="0.45" stop-color="#7f8c98"/>
        <stop offset="0.7" stop-color="#2c3742"/>
        <stop offset="1" stop-color="#d5bfa9"/>
      </linearGradient>
    </defs>
    <polygon points="0,0 70,0 0,95" fill="#ffffff"/>
    <polygon points="0,95 50,95 275,392 226,392" fill="var(--red)"/>
    <polygon role="img" aria-label="Hand holding a phone showing a residential tower"
      points="0,118 36,118 232,392 0,392" fill="url(#hand)"/>
  </svg>

  <p class="abs choose">
    <span class="big">CHOOSE</span>
    <span class="sub">from over 3,700 apartments</span>
    <span class="sub">in Chicago’s most celebrated</span>
    <span class="hood">NEIGHBORHOODS</span>
  </p>

  <svg class="abs phone-icon" width="50" height="50" viewBox="0 0 48 48" aria-hidden="true">
    <circle cx="24" cy="24" r="24" fill="var(--ink)"/>
    <path d="M17 13c1.5-1 3-.5 3.6.8l1.8 3.8c.5 1-.1 2-.9 2.6l-1.3 1c1 2.6 3 4.6 5.6 5.6l1-1.3c.6-.8 1.6-1.4 2.6-.9l3.8 1.8c1.3.6 1.8 2.1.8 3.6-1.4 2.1-3.4 3-5.7 2.4-6.2-1.7-11-6.5-12.7-12.7-.6-2.3.3-4.3 2.4-5.7z" fill="#fff"/>
    <path d="M27 14a8 8 0 0 1 7 7M27 18a4 4 0 0 1 3 3" stroke="#fff" stroke-width="1.8" fill="none" stroke-linecap="round"/>
  </svg>
  <p class="abs phone-number">773-582-6041</p>

  <div class="abs brand"><span>KVT</span><span class="mark"></span></div>

  <p class="abs url-bar">www.kvtresidences.example</p>
</main>
</body>
</html>
```